Meadowlark Learning Growth Partners (MLGP)

This is a professional business card. Logo and picture are a must on the front of the card. I am an educational consultant. I have been consulting for the past three years for a company. I am now opening my own company. My goal for my consulting company is to eventually consult all over America.

Target Market(s)

Educators, schools, professionals

Industry/Entity Type

Consulting

Contact Information for Business Card

Picture/logo on front, simple modern design

Font styles to use
Serif

Colors
85abd2
0355a3
3176b5
cedeed

Requirements
Must have
• picture, logo,
• Odessa Pruitt, Ed.S
• address 5073 Cormorant ridge Dr. Nashville, TN 37940
• Cell:616-555-0148
• Office: 629-555-0172
• www.Mlgpedu.example
• pruittodessa@mailbox.example

```html
<!DOCTYPE html>
<html lang="en">
<head>
<meta charset="utf-8">
<title>MLGP - Odessa Pruitt - Business Card</title>
<link rel="stylesheet" href="https://fonts.googleapis.com/css2?family=Source+Sans+3:wght@400&family=Tinos:wght@400;700&display=swap">
<style>
  :root {
    --page: #ffffff;
    --card: #ede7d8;
    --stripe: #85abd2;
    --navy: #0a3b78;
    --ink: #2b5592;
    --label: #111111;
    --photo-top: #3176b5;
    --photo-bottom: #1f4f9a;
  }
  * { margin: 0; padding: 0; box-sizing: border-box; }
  html, body { width: 1200px; height: 797px; overflow: hidden; background: var(--page); }
  .sheet { position: relative; width: 1200px; height: 797px; }

  .sheet-title {
    position: absolute; left: 74px; top: 52px;
    font-family: "Source Sans 3", sans-serif; font-size: 19.5px; line-height: 26px;
    color: var(--label);
  }

  .card {
    position: absolute; top: 246px; width: 254px; height: 445px;
    background: var(--card);
  }
  .card-front { left: 338px; }
  .card-back { left: 633px; }

  .top-stripe { position: absolute; left: 0; top: 16px; width: 100%; height: 6px; background: var(--stripe); }

  .brand { position: absolute; left: 17px; top: 38px; display: flex; align-items: center; height: 52px; }
  .brand-dot { width: 46px; height: 46px; border-radius: 50%; background: var(--navy); }
  .brand-short {
    margin-left: 10px; font-family: "Tinos", serif; font-weight: 700;
    font-size: 20px; letter-spacing: 1.5px; color: var(--navy);
  }
  .brand-divider { width: 1px; height: 52px; background: var(--navy); margin-left: 8px; }
  .brand-full {
    margin-left: 7px; font-family: "Tinos", serif; font-weight: 700;
    font-size: 10.5px; line-height: 13.5px; color: var(--navy);
  }

  .portrait {
    position: absolute; left: 83px; top: 106px; width: 90px; height: 112px;
    background: linear-gradient(180deg, var(--photo-top), var(--photo-bottom));
  }

  .contact {
    position: absolute; left: 0; width: 100%; text-align: center;
    font-family: "Tinos", serif; color: var(--ink);
  }
  .holder-name { top: 233px; font-size: 14.5px; font-weight: 700; color: var(--navy); letter-spacing: 0.2px; }
  .address { top: 265px; font-size: 14px; line-height: 21.5px; }
  .phones { top: 317px; font-size: 14px; line-height: 21.5px; }
  .online { top: 381px; font-size: 14px; line-height: 21.5px; }

  .back-mark {
    position: absolute; left: 0; top: 0; width: 100%; height: 100%;
    display: flex; flex-direction: column; align-items: center;
  }
  .back-dot { margin-top: 95px; width: 150px; height: 150px; border-radius: 50%; background: var(--navy); }
  .back-name {
    margin-top: 20px; font-family: "Tinos", serif; font-weight: 700;
    font-size: 58px; line-height: 1; letter-spacing: 4px; color: var(--navy);
  }

  .side-label {
    position: absolute; top: 698px; font-family: "Source Sans 3", sans-serif;
    font-size: 19.5px; color: var(--label); transform: translateX(-50%);
  }
  .label-front { left: 442px; }
  .label-back { left: 754px; }
</style>
</head>
<body>
<div class="sheet">
  <div class="sheet-title">MLGP - Odessa Pruitt - Business Card<br>Design 2&nbsp; - Portrait</div>

  <section class="card card-front">
    <div class="top-stripe"></div>
    <div class="brand">
      <div class="brand-dot"></div>
      <div class="brand-short">MLGP</div>
      <div class="brand-divider"></div>
      <div class="brand-full">Meadowlark<br>Learning<br>Growth<br>Partners</div>
    </div>
    <div class="portrait" role="img" aria-label="Portrait photo of Odessa Pruitt against a blue backdrop"></div>
    <div class="contact holder-name">ODESSA PRUITT, Ed. S</div>
    <div class="contact address">5073 Cormorant Ridge Drive<br>Nashville, TN 37940</div>
    <div class="contact phones">Cell: (616) 555-0148<br>Office: (629) 555-0172</div>
    <div class="contact online">www.mlgpedu.example<br>pruittodessa@mailbox.example</div>
  </section>

  <section class="card card-back">
    <div class="back-mark">
      <div class="back-dot"></div>
      <div class="back-name">MLGP</div>
    </div>
  </section>

  <div class="side-label label-front">Front</div>
  <div class="side-label label-back">Back</div>
</div>
</body>
</html>
```